High Tech Software Company Needs MOVIE POSTER

We need a poster design for theme for our 2016 kick off event for the sales team. Our software company is based in TORONTO & BOSTON and we essentially do 'crowdsourcing' for referrals, references, and reviews.

Our domain is www.brackenvale.com check it out to see our culture and our logo to be used in the design.

The THEME of our kick off is "ALL IN!" we would like to see the design use our logo and be creative and AWESOME potentially a poster that represents a movie? The design needs to inspire people, it needs to get them excited.

its only for internal use there is no issue about copywrite

Target Market(s)

These posters will be in all of our offices, Toronto, Boston, Palo Alto, and San Fran

Industry/Entity Type

Movie

Requirements
Must have
• The theme on it, "All In". it must be a motivating image. it is a theme commonly used in poker, "I'm All in!" pushing all their poker chips into the game. Check out some images on that. using the brackenvale logo (in the poker chips?) Maybe the poker table with the brackenvale logo? We will supply the names but the poster should also have the MOVIE theme see attached poster for making it "movie like" with names and the credits that are commonly found on movie posters. THE ATTACHMENT IS FROM A PREVIOUS CONTEST. SHOWN STRICTLY FOR THE MOVIE POSTER THEME CONTENT IS NOT RELEVANT!!!
Nice to have
• Its for a sales team so obviously the "all in" has to be motivating.

```html
<!DOCTYPE html>
<html lang="en">
<head>
<meta charset="utf-8">
<title>All In — Brackenvale Kick Off Poster</title>
<link rel="stylesheet" href="https://fonts.googleapis.com/css2?family=Monoton&family=Oswald:wght@300;400&family=Cinzel:wght@600&display=swap">
<style>
  :root {
    --backdrop: #6e6f73;
    --poster-black: #050506;
    --felt-green: #1f4a44;
    --felt-deep: #0d2523;
    --gold: #f2b91f;
    --gold-light: #ffe27a;
    --gold-dark: #8a5a06;
    --text-light: #e9e9ea;
    --mark-blue: #1ea3df;
  }
  html, body {
    margin: 0;
    width: 1200px;
    height: 1000px;
    overflow: hidden;
    background: var(--backdrop);
  }
  .poster {
    position: absolute;
    left: 278px;
    top: 27px;
    width: 644px;
    height: 945px;
    background: var(--poster-black);
    overflow: hidden;
    box-shadow: 0 2px 6px rgba(0,0,0,0.45);
    font-family: "Oswald", "Arial Narrow", sans-serif;
    color: var(--text-light);
  }
  .hero-photo {
    position: absolute;
    left: 0; top: 0;
    width: 644px; height: 440px;
    background:
      radial-gradient(ellipse 60% 40% at 52% 68%, rgba(60,120,130,0.85), transparent 70%),
      radial-gradient(ellipse 30% 18% at 40% 52%, rgba(200,80,90,0.55), transparent 70%),
      radial-gradient(ellipse 25% 15% at 70% 40%, rgba(170,130,110,0.45), transparent 70%),
      linear-gradient(180deg, #0b0c10 0%, #1b2226 40%, var(--felt-green) 72%, var(--felt-deep) 100%);
  }
  .table-edge {
    position: absolute;
    left: 0; top: 400px;
    width: 644px; height: 120px;
  }
  .billing-banner {
    position: absolute;
    left: 140px; top: 59px;
    width: 364px; height: 20px;
    border: 2px solid var(--gold);
    border-radius: 3px;
    background: #0a0a0a;
    box-sizing: border-box;
    text-align: center;
    font-family: "Cinzel", serif;
    font-weight: 600;
    font-size: 10.5px;
    letter-spacing: 2.2px;
    line-height: 16px;
    color: var(--gold-light);
  }
  .title {
    position: absolute;
    left: 0; top: 440px;
    width: 644px;
    margin: 0;
    text-align: center;
    font-family: "Monoton", cursive;
    font-weight: 400;
    font-size: 226px;
    line-height: 240px;
    letter-spacing: 2px;
    word-spacing: 40px;
    color: var(--gold);
    text-shadow: 0 0 2px var(--gold-light), 0 3px 8px rgba(138,90,6,0.8);
    transform: scaleX(0.6);
    transform-origin: center;
    white-space: nowrap;
  }
  .title-glow {
    position: absolute;
    left: 0; top: 650px;
    width: 644px; height: 60px;
  }
  .damask-band {
    position: absolute;
    left: 100px; top: 700px;
    width: 444px; height: 100px;
    background: radial-gradient(ellipse at center, #1e1e22 0%, #0c0c0e 60%, transparent 80%);
  }
  .brand {
    position: absolute;
    left: 0; top: 734px;
    width: 644px;
    display: flex;
    justify-content: center;
    align-items: center;
    gap: 10px;
  }
  .brand-mark {
    width: 40px; height: 40px;
    border-radius: 50%;
    background: var(--mark-blue);
  }
  .brand-name {
    font-family: "Oswald", sans-serif;
    font-weight: 400;
    font-size: 40px;
    line-height: 1;
    color: #ffffff;
  }
  .credits {
    position: absolute;
    left: 0; top: 818px;
    width: 644px;
    text-align: center;
    text-transform: uppercase;
    font-weight: 300;
  }
  .credit-line {
    margin: 0;
    font-size: 16px;
    line-height: 22px;
    letter-spacing: 0.2px;
    white-space: nowrap;
  }
  .credit-line.small-line { font-size: 14.5px; }
  .role {
    display: inline-block;
    font-size: 6.5px;
    line-height: 7px;
    text-transform: lowercase;
    vertical-align: middle;
    text-align: right;
    margin: 0 3px 0 6px;
  }
  .joiner {
    font-size: 7px;
    text-transform: lowercase;
    margin: 0 4px;
    vertical-align: middle;
  }
</style>
</head>
<body>
  <main class="poster">
    <div class="hero-photo" role="img" aria-label="Poker player's hands in suit sleeves pushing stacks of red, blue, green and black chips across a green felt table"></div>

    <svg class="table-edge" viewBox="0 0 644 120" aria-hidden="true">
      <defs>
        <linearGradient id="edgeShade" x1="0" y1="0" x2="0" y2="1">
          <stop offset="0" stop-color="#050506" stop-opacity="0"/>
          <stop offset="0.45" stop-color="#050506" stop-opacity="0.95"/>
          <stop offset="1" stop-color="#050506"/>
        </linearGradient>
        <linearGradient id="rimLight" x1="0" y1="0" x2="1" y2="0">
          <stop offset="0" stop-color="#ffffff" stop-opacity="0"/>
          <stop offset="0.5" stop-color="#ffffff" stop-opacity="0.9"/>
          <stop offset="1" stop-color="#ffffff" stop-opacity="0"/>
        </linearGradient>
      </defs>
      <rect x="0" y="0" width="644" height="120" fill="url(#edgeShade)"/>
      <path d="M0 58 Q322 20 644 58 L644 120 L0 120 Z" fill="#0b0b0d"/>
      <path d="M0 58 Q322 20 644 58" fill="none" stroke="url(#rimLight)" stroke-width="1.5"/>
    </svg>

    <div class="billing-banner">-Brackenvale Productions Presents-</div>

    <h1 class="title">ALL IN</h1>

    <svg class="title-glow" viewBox="0 0 644 60" aria-hidden="true">
      <defs>
        <radialGradient id="flare" cx="0.5" cy="0.5" r="0.5">
          <stop offset="0" stop-color="#ffffff" stop-opacity="0.9"/>
          <stop offset="1" stop-color="#ffffff" stop-opacity="0"/>
        </radialGradient>
      </defs>
      <path d="M60 40 Q322 22 584 40" fill="none" stroke="#ffffff" stroke-opacity="0.35" stroke-width="1"/>
      <ellipse cx="300" cy="31" rx="70" ry="4" fill="url(#flare)"/>
    </svg>

    <div class="damask-band" role="img" aria-label="Faint dark damask pattern behind the company name"></div>

    <div class="brand">
      <span class="brand-mark" aria-hidden="true"></span>
      <span class="brand-name">brackenvale</span>
    </div>

    <section class="credits">
      <p class="credit-line">Northwire <span class="joiner">in association with</span> Stillmere <span class="joiner">and</span> Korvel Productions <span class="joiner">presents a film by</span> Mira Tal-Oren</p>
      <p class="credit-line">“Bright Signal” <span class="role">executive<br>producers</span> Ada Lund &nbsp;Jean Harte &nbsp;Carl Vent <span class="role">director of<br>photography</span> Elan Moor <span class="joiner">editor</span> Thomas Renick</p>
      <p class="credit-line"><span class="role">original<br>score</span> Nils Vander <span class="role">associate<br>producers</span> Lena Marchetti &nbsp;Thomas Renick &nbsp;Peter Aldous</p>
      <p class="credit-line small-line"><span class="joiner">introducing</span> Rolf Aster <span class="joiner">co-producer</span> Sofia Bellan <span class="role">produced and<br>directed by</span> Mira Tal-Oren</p>
    </section>
  </main>
</body>
</html>
```